Business Card Design

We offer Procurement, Supply Chain, Merchandise Expediting, Customs Management, Shipping Documentation and many other Specialized Consultancies. The many products we handle are used in many different industries like Oil, Gas and Drilling Hardware, Construction Equipment, Industrial Parts and much more.
Our Slogan is:
"We look from around the world for what you need, bringing it to your door in the shortest possible time with the best all inclusive price"

Target Market(s)

US Export companies, Mexican Import companies and others companies that are looking for Oil & Gas products

Industry/Entity Type

Business

Contact Information for Business Card

Corvinet Trade Partners & Providers, LLC
Phone: +1 (555) 014-0193
31542 Larkfield Pkwy, Ste 1800
Brennick, Ohio 44000 USA
www.corvinet.biz

Font styles to use
Other font styles liked:
• Century Gothic

```html
<!DOCTYPE html>
<html lang="en">
<head>
<meta charset="utf-8">
<title>Corvinet Trade Partners &amp; Providers — Business Card</title>
<link rel="stylesheet" href="https://fonts.googleapis.com/css2?family=Lato:wght@400;700&display=swap">
<style>
  :root {
    --stage: #2f2a28;
    --card-black: #0a0a0a;
    --card-light: #ececec;
    --brand-red: #e8403f;
    --brand-green: #0f7a4b;
    --ink: #1e1e1e;
    --paper-white: #ffffff;
    --accent-faint: #f2c4b6;
  }
  html, body {
    margin: 0;
    padding: 0;
    width: 1200px;
    height: 716px;
    overflow: hidden;
    background: var(--stage);
    font-family: "Lato", sans-serif;
  }
  .canvas {
    position: relative;
    width: 1200px;
    height: 716px;
  }
  .card {
    position: absolute;
    top: 215px;
    width: 500px;
    height: 286px;
    border-radius: 4px;
    overflow: hidden;
    box-shadow: 0 10px 24px rgba(0,0,0,0.45);
  }
  .card--back {
    left: 70px;
    background: var(--card-black);
  }
  .card--front {
    left: 630px;
    background: var(--card-light);
  }
  .name-block {
    position: absolute;
    display: flex;
    align-items: center;
    gap: 10px;
  }
  .name-block__dot {
    width: 14px;
    height: 14px;
    border-radius: 50%;
    background: var(--brand-green);
  }
  .name-block__name {
    font-weight: 700;
    font-size: 30px;
    line-height: 1;
    letter-spacing: 3px;
    text-transform: uppercase;
  }
  .card--back .name-block {
    left: 130px;
    top: 126px;
  }
  .card--back .name-block__name { color: var(--paper-white); }
  .card--front .name-block {
    left: 28px;
    top: 30px;
  }
  .card--front .name-block__dot { width: 11px; height: 11px; }
  .card--front .name-block__name {
    font-size: 22px;
    letter-spacing: 2px;
    color: var(--ink);
  }
  .card__art {
    position: absolute;
    left: 0;
    top: 0;
    width: 500px;
    height: 286px;
  }
  .contact {
    position: absolute;
    left: 70px;
    top: 82px;
    color: var(--ink);
    font-size: 10.5px;
    line-height: 1.5;
  }
  .contact__company {
    font-weight: 700;
    font-size: 13px;
    margin: 0 0 3px;
  }
  .contact__line { margin: 0; }
</style>
</head>
<body>
<main class="canvas">
  <section class="card card--back" aria-label="Card back">
    <div class="name-block">
      <span class="name-block__dot"></span>
      <span class="name-block__name">Corvinet</span>
    </div>
  </section>

  <section class="card card--front" aria-label="Card front">
    <svg class="card__art" viewBox="0 0 500 286" aria-hidden="true">
      <polygon class="band-red" points="0,176 500,176 500,232 0,232" fill="var(--brand-red)"/>
      <rect class="faint-square" x="400" y="150" width="80" height="78" rx="10" fill="var(--accent-faint)" opacity="0.55"/>
      <polygon class="band-divider" points="0,208 250,208 262,220 500,220 500,226 262,226 250,214 0,214" fill="var(--paper-white)"/>
      <polygon class="band-green" points="0,214 250,214 262,226 500,226 500,286 0,286" fill="var(--brand-green)"/>
    </svg>
    <div class="name-block">
      <span class="name-block__dot"></span>
      <span class="name-block__name">Corvinet</span>
    </div>
    <div class="contact">
      <p class="contact__company">Corvinet Trade Partners &amp; Providers, LLC</p>
      <p class="contact__line">+1 (555) 014-0193</p>
      <p class="contact__line">www.corvinet.biz</p>
      <p class="contact__line">31542 Larkfield Pkwy, Ste 1800 Brennick, Ohio 44000 USA</p>
    </div>
  </section>
</main>
</body>
</html>
```